Banner ad design for Vantora Display Ads

We are looking for a designer to develop a concept for banner ads for a Vantora Display campaign we are building.

We have 3 business lines, shredding services, records management services and scanning services.

We are looking for 4 sets of ads to be created, one for each business line + one set that showcases all of our lines together.

For the design concepts, we would like to see a few sizes (banner, square, leaderboard, skyscraper, etc) for each.

The person chosen will then need to create the ads into all Vantora supported sizes -- 20 sizes total for each set of ads as per the Vantora size guidelines found on this page - https://help.vantora-example.com/vantora-ads/answer/4827150?hl=en&ref_topic=6604821#

A few items to note:
- Design should complement our existing brand/website look and feel (www.oak-ferry.ca)
- Each final ad must be 150Kb or less in size
- Final designs should be editable, meaning if we would like to change some copy in the design, we can do so using a well-known software (Canva, Photoshop/InDesign, etc)
- Some images are attached for use, but if you feel a different stock image is more suitable to to your design, please go ahead and use it.

Provided below is some messaging that can be used for each set of ads. Do not feel you need to use all of the messaging, it is provided for guidance.

SHREDDING SERVICES:

Possible Short Headline:
-- One-Time Shredding Services
-- Secure Shredding Services
-- Affordable On-Site Shredding

Possible Long Headline
-- Your Paper Can be Destroyed as Soon as the Next Business Day

Possible Descriptions:
-- KVEC Gold Certified On site shredding company. Service as soon as Next Day.
-- Secure and Affordable Toronto & GTA On-Site Shredding.
-- Certified, Affordable Office Shredding Since 2003.
-- Quick, no contact and affordable paper shredding services in Toronto & Southern Ontario.
-- Certified, Affordable Office Shredding Since 2003. Fast, no contact shredding service.

Call to Action
-- Get a Quote

RECORDS MANAGEMENT
Short Headline:
-- Off-site Records Storage
-- Records Management & Storage
-- Secure Records Storage
-- Records Management Services
-- Long Term Records Management
-- Document Storage Solutions

Possible Description
-- Local, Affordable Storage Solutions. Protect and Store your Documents in our Secure Facility
-- Local, Affordable Records Management Solutions. Store your Records in our Secure Facility
-- Certified, Affordable Document Storage Since 2004. Contact Us for a Free Quote!
-- Vaultline+ Certified, Affordable Document Storage Since 2004. Contact Us for a Free Quote!

Call to Action
-- Get a Quote

SCANNING SERVICES

Short Headline:
-- Professional Scanning Company
-- Toronto & GTA Scanning Service
-- Document Scanning Services
-- Digital Conversion Services
-- Fast & Easy Retrieval

Description
-- Scan and documents and files with Professional scanning services from Oak-Ferry
-- Convert Your Paper Files to Electronic Files. Fast & Easy Retrieval.
-- Easily access your documents electronically with Document Scanning Services

Call to Action
-- Get a Quote

ALL SERVICES AD SET
Short Headline
-- Shred, Scan & Store Documents
-- Secure Shredding, Records Management and Scanning Services
-- #1 Document Management Company
-- Oak Ferry Shredding, Storage & Scanning

Description
-- Secure and Affordable Toronto & GTA On-Site Shredding, Document Storage & Scanning Company

Call to Action
-- Get a Quote

Font styles to use
Sans Serif

```html
<!DOCTYPE html>
<html lang="en">
<head>
<meta charset="utf-8">
<title>Oak-Ferry Display Ad Set</title>
<link href="https://fonts.googleapis.com/css2?family=Open+Sans:wght@700;800&family=PT+Sans:wght@400;700&display=swap" rel="stylesheet">
<style>
  :root {
    --navy: #031537;
    --white: #ffffff;
    --brand-blue: #1a93d8;
    --brand-blue-light: #5db9ee;
    --ink: #1b1b1b;
    --cta-green: #16b84a;
  }
  * { margin: 0; padding: 0; box-sizing: border-box; }
  html, body { width: 1200px; height: 1200px; overflow: hidden; }
  body { background: var(--navy); position: relative; font-family: "PT Sans", Arial, sans-serif; }

  .banner {
    position: absolute; left: 120px; width: 961px; height: 247px;
    background: var(--white); overflow: hidden;
  }
  .banner--all { top: 91px; width: 958px; }
  .banner--scanning { top: 356px; }
  .banner--records { top: 620px; }
  .banner--shredding { top: 886px; }

  .banner__art { position: absolute; inset: 0; width: 100%; height: 100%; }

  .brand { position: absolute; left: 30px; top: 24px; }
  .brand__name {
    display: flex; align-items: center; gap: 6px;
    font-family: "Open Sans", Arial, sans-serif; font-weight: 800;
    font-size: 25px; line-height: 1; color: var(--brand-blue); letter-spacing: -0.5px;
  }
  .brand__mark { width: 10px; height: 10px; background: var(--brand-blue); }
  .brand__tagline { margin-top: 4px; font-size: 14px; color: var(--ink); letter-spacing: 0.4px; }

  .headline {
    position: absolute; left: 28px;
    font-family: "Open Sans", Arial, sans-serif; font-weight: 800;
    color: var(--brand-blue); line-height: 1.05; letter-spacing: -0.2px;
  }
  .subline { position: absolute; left: 28px; color: var(--brand-blue); font-size: 21px; line-height: 1.18; }
  .banner--all .headline { top: 101px; font-size: 27px; left: 30px; }
  .banner--all .subline { top: 136px; font-size: 19.5px; left: 30px; }
  .banner--scanning .headline,
  .banner--records .headline { top: 108px; font-size: 34px; }
  .banner--scanning .subline,
  .banner--records .subline { top: 149px; }
  .banner--shredding .headline { top: 102px; font-size: 32px; }
  .banner--shredding .subline { top: 175px; }

  .cta {
    position: absolute; width: 127px; height: 44px; border-radius: 8px;
    background: var(--cta-green); color: var(--white);
    font-family: "Open Sans", Arial, sans-serif; font-weight: 700; font-size: 16px;
    display: flex; align-items: center; justify-content: center;
    box-shadow: 0 3px 6px rgba(0,0,0,0.25);
  }
  .banner--all .cta { left: 388px; top: 37px; }
  .banner--scanning .cta,
  .banner--records .cta,
  .banner--shredding .cta { left: 819px; top: 14px; }

  .service-label {
    position: absolute; color: var(--white);
    font-family: "Open Sans", Arial, sans-serif; font-weight: 800;
    font-size: 17px; line-height: 0.95;
  }
  .service-label--shredding { left: 584px; top: 18px; }
  .service-label--scanning { left: 835px; top: 18px; }
  .service-label--records { left: 784px; top: 206px; }
</style>
</head>
<body>

<!-- All services -->
<section class="banner banner--all">
  <svg class="banner__art" viewBox="0 0 958 247" preserveAspectRatio="none">
    <defs>
      <linearGradient id="shredScene" x1="0" y1="0" x2="1" y2="1">
        <stop offset="0" stop-color="#cfe6f3"/><stop offset="1" stop-color="#e9eef1"/>
      </linearGradient>
      <linearGradient id="storeScene" x1="0" y1="0" x2="0" y2="1">
        <stop offset="0" stop-color="#d9d4c8"/><stop offset="0.5" stop-color="#d8c46a"/><stop offset="1" stop-color="#3a3f46"/>
      </linearGradient>
      <linearGradient id="scanScene" x1="0" y1="0" x2="1" y2="1">
        <stop offset="0" stop-color="#c8d3dc"/><stop offset="1" stop-color="#8a96a2"/>
      </linearGradient>
    </defs>
    <polygon points="535,0 958,0 958,247 543,247 585,130" fill="var(--brand-blue)"/>
    <g role="img" aria-label="Hand placing paper into a secure shredding bin">
      <polygon points="700,0 755,0 780,190 760,247 625,247 650,100" fill="url(#shredScene)"/>
    </g>
    <g role="img" aria-label="Office with stacked files and storage boxes">
      <polygon points="775,0 820,0 862,190 790,190" fill="url(#storeScene)"/>
    </g>
    <g role="img" aria-label="Technician feeding documents into a scanner">
      <polygon points="880,68 958,60 958,247 935,247" fill="url(#scanScene)"/>
    </g>
    <polygon points="755,0 775,0 790,190 780,190" fill="var(--brand-blue-light)" opacity="0.8"/>
  </svg>
  <div class="brand">
    <div class="brand__name">oak-ferry<span class="brand__mark"></span></div>
    <div class="brand__tagline">Information Security</div>
  </div>
  <div class="cta">GET A QUOTE</div>
  <h1 class="headline">#1 Document Management Company</h1>
  <p class="subline">Secure and Affordable Toronto &amp; GTA On-Site Shredding,<br>Document Storage &amp; Scanning Company</p>
  <span class="service-label service-label--shredding">Shredding<br>Services</span>
  <span class="service-label service-label--scanning">Scanning<br>Services</span>
  <span class="service-label service-label--records">Records<br>Management</span>
</section>

<!-- Scanning -->
<section class="banner banner--scanning">
  <svg class="banner__art" viewBox="0 0 961 247" preserveAspectRatio="none">
    <defs>
      <linearGradient id="scanPhoto" x1="0" y1="0" x2="1" y2="1">
        <stop offset="0" stop-color="#d8d4cc"/><stop offset="0.6" stop-color="#c6c9cc"/><stop offset="1" stop-color="#8d9196"/>
      </linearGradient>
    </defs>
    <polygon points="603,0 961,0 961,247 720,247" fill="var(--brand-blue)"/>
    <g role="img" aria-label="Technician loading documents into a scanner at an office desk">
      <polygon points="650,0 961,0 961,247 750,247 700,140" fill="url(#scanPhoto)"/>
    </g>
  </svg>
  <div class="brand">
    <div class="brand__name">oak-ferry<span class="brand__mark"></span></div>
    <div class="brand__tagline">Information Security</div>
  </div>
  <h2 class="headline">Professional Scanning Company</h2>
  <p class="subline">Easily access your documents electronically with Document<br>Scanning Services</p>
  <div class="cta">GET A QUOTE</div>
</section>

<!-- Records -->
<section class="banner banner--records">
  <svg class="banner__art" viewBox="0 0 961 247" preserveAspectRatio="none">
    <defs>
      <linearGradient id="recordsPhoto" x1="0" y1="0" x2="0" y2="1">
        <stop offset="0" stop-color="#e6e7e8"/><stop offset="0.35" stop-color="#b9a98e"/><stop offset="0.6" stop-color="#e0c24a"/><stop offset="1" stop-color="#3b3f45"/>
      </linearGradient>
    </defs>
    <polygon points="603,0 961,0 961,247 720,247" fill="var(--brand-blue)"/>
    <g role="img" aria-label="Records storage office with stacked files and yellow archive boxes">
      <polygon points="650,0 961,0 961,247 750,247 700,140" fill="url(#recordsPhoto)"/>
    </g>
  </svg>
  <div class="brand">
    <div class="brand__name">oak-ferry<span class="brand__mark"></span></div>
    <div class="brand__tagline">Information Security</div>
  </div>
  <h2 class="headline">Records Management Services</h2>
  <p class="subline">Local, Affordable Records Management Solutions. Store your<br>Records in our Secure Facility</p>
  <div class="cta">GET A QUOTE</div>
</section>

<!-- Shredding -->
<section class="banner banner--shredding">
  <svg class="banner__art" viewBox="0 0 961 247" preserveAspectRatio="none">
    <defs>
      <linearGradient id="officeFade" x1="0" y1="0" x2="0" y2="1">
        <stop offset="0" stop-color="#eef0f2"/><stop offset="1" stop-color="#ffffff"/>
      </linearGradient>
      <linearGradient id="shredPhoto" x1="0" y1="0" x2="1" y2="1">
        <stop offset="0" stop-color="#dfe3e6"/><stop offset="0.6" stop-color="#f1f3f4"/><stop offset="1" stop-color="#9fdcf2"/>
      </linearGradient>
    </defs>
    <g role="img" aria-label="Faded bright office with a worker at a shredding bin">
      <rect x="246" y="0" width="360" height="120" fill="url(#officeFade)"/>
    </g>
    <polygon points="603,0 961,0 961,247 720,247" fill="var(--brand-blue)"/>
    <g role="img" aria-label="Hand dropping paper into a locked shredding console">
      <polygon points="650,0 961,0 961,247 750,247 700,140" fill="url(#shredPhoto)"/>
    </g>
  </svg>
  <div class="brand">
    <div class="brand__name">oak-ferry<span class="brand__mark"></span></div>
    <div class="brand__tagline">Information Security</div>
  </div>
  <h2 class="headline">Your Paper Can be Destroyed<br>as Soon as the Next Business Day</h2>
  <p class="subline">Quick, no contact and affordable paper shredding services in<br>Toronto &amp; Southern Ontario.</p>
  <div class="cta">GET A QUOTE</div>
</section>

</body>
</html>
```